KALVERIA Consultancy Business Card

We need a business card design for a new Image & Etiquette Consultancy Company.

The design should reflect the corporate colour found in the logo attached.

Info to include:

Name: Melba Tran
Title: Image Consultant
Company: KAL VERIA CONSULTANCY
Address: 27 Kelso Street, #14-09 Harbourline Tower, Singapore 058217
Contact: 9317 6284
Email: melba@kalveria.com.sg
Website: www.kalveria.com.sg

```html
<!DOCTYPE html>
<html lang="en">
<head>
<meta charset="utf-8">
<title>KALVERIA Consultancy – Business Card</title>
<link rel="stylesheet" href="https://fonts.googleapis.com/css2?family=Ubuntu:wght@400;500;700&display=swap">
<style>
  :root {
    --stage: #ebe7e2;
    --purple: #2d1048;
    --gold: #d6a628;
    --gold-light: #efc64a;
    --gold-dark: #b8841c;
    --silver: #d9d9dc;
    --white: #ffffff;
    --text-light: #f1ecf5;
    --edge: #3a3a3a;
  }
  * { box-sizing: border-box; margin: 0; padding: 0; }
  html, body {
    width: 1200px;
    height: 1080px;
    overflow: hidden;
    background: var(--stage);
    font-family: "Ubuntu", sans-serif;
  }
  .canvas { position: relative; width: 1200px; height: 1080px; }

  .card {
    position: absolute;
    width: 822px;
    height: 474px;
    border-radius: 28px;
    overflow: hidden;
  }

  /* ---------- Front ---------- */
  .card--front {
    left: 318px;
    top: 44px;
    background: var(--purple);
    box-shadow: 0 6px 18px rgba(0,0,0,0.18);
  }
  .brand {
    position: absolute;
    left: 0;
    width: 100%;
    text-align: center;
    color: var(--gold);
    font-weight: 400;
    line-height: 1;
  }
  .card--front .brand { top: 78px; }
  .brand__name { display: block; font-size: 64px; letter-spacing: 4px; }
  .brand__sub { display: block; font-size: 21px; letter-spacing: 6px; margin-top: 12px; }

  .contact {
    position: absolute;
    top: 222px;
    left: 0;
    width: 100%;
    color: var(--text-light);
    font-size: 18px;
    line-height: 36px;
  }
  .contact__address {
    position: absolute;
    right: 464px;
    text-align: right;
    white-space: nowrap;
    font-style: normal;
  }
  .contact__divider {
    position: absolute;
    left: 377px;
    top: 0;
    width: 1.5px;
    height: 108px;
    background: rgba(255,255,255,0.55);
  }
  .contact__lines {
    position: absolute;
    left: 398px;
    list-style: none;
  }
  .contact__lines li { display: flex; align-items: center; gap: 8px; white-space: nowrap; }
  .contact__icon { width: 17px; height: 17px; flex: none; }

  .accent-band {
    position: absolute;
    left: 0;
    right: 0;
    top: 384px;
    bottom: 0;
    background: linear-gradient(90deg, #c9c9ce 0%, #f4f4f6 28%, #e3c25a 55%, var(--gold-light) 75%, var(--gold-dark) 100%);
  }

  .person {
    position: absolute;
    left: 520px;
    width: 214px;
    top: 394px;
    text-align: center;
    color: var(--white);
  }
  .person__name { font-size: 24px; font-weight: 500; line-height: 32px; }
  .person__title { font-size: 20px; font-weight: 400; line-height: 30px; }

  /* ---------- Back ---------- */
  .card--back {
    left: 56px;
    top: 555px;
    background: var(--white);
    border: 1.5px solid var(--edge);
  }
  .card--back .brand { top: 152px; color: var(--purple); }
  .card--back .brand__name { font-size: 78px; letter-spacing: 6px; }
  .card--back .brand__sub { font-size: 25px; letter-spacing: 8px; margin-top: 14px; }
  .website {
    position: absolute;
    top: 368px;
    width: 100%;
    text-align: center;
    color: var(--purple);
    font-size: 24px;
    letter-spacing: 2px;
  }
  .website strong { font-weight: 500; }
</style>
</head>
<body>
<main class="canvas">

  <section class="card card--front" aria-label="Business card front">
    <div class="accent-band" role="img" aria-label="Decorative silver and gold wave band"></div>

    <div class="brand">
      <span class="brand__name">KAL VERIA</span>
      <span class="brand__sub">CONSULTANCY</span>
    </div>

    <div class="contact">
      <address class="contact__address">
        27 Kelso Street<br>
        #14-09 Harbourline Tower<br>
        Singapore 058217
      </address>
      <span class="contact__divider"></span>
      <ul class="contact__lines">
        <li>
          <svg class="contact__icon" viewBox="0 0 20 20" aria-hidden="true">
            <circle cx="10" cy="10" r="10" fill="#d6a628"/>
            <path d="M6.5 5.5 l2 0 l1 3 l-1.4 1 a6 6 0 0 0 2.9 2.9 l1-1.4 l3 1 l0 2 a1.2 1.2 0 0 1 -1.3 1.1 A9 9 0 0 1 5.4 6.8 A1.2 1.2 0 0 1 6.5 5.5 Z" fill="#2d1048"/>
          </svg>
          <span>9317 6284</span>
        </li>
        <li>
          <svg class="contact__icon" viewBox="0 0 20 20" aria-hidden="true">
            <circle cx="10" cy="10" r="10" fill="#d6a628"/>
            <rect x="4.5" y="6.5" width="11" height="7.5" rx="1" fill="#2d1048"/>
            <path d="M4.8 7 L10 11 L15.2 7" fill="none" stroke="#d6a628" stroke-width="1.2"/>
          </svg>
          <span>melba@kalveria.com.sg</span>
        </li>
        <li>
          <svg class="contact__icon" viewBox="0 0 20 20" aria-hidden="true">
            <circle cx="10" cy="10" r="10" fill="#d6a628"/>
            <circle cx="10" cy="10" r="5.5" fill="none" stroke="#2d1048" stroke-width="1.3"/>
            <ellipse cx="10" cy="10" rx="2.3" ry="5.5" fill="none" stroke="#2d1048" stroke-width="1.1"/>
            <path d="M4.5 10 H15.5" stroke="#2d1048" stroke-width="1.1"/>
          </svg>
          <span>www.kalveria.com.sg</span>
        </li>
      </ul>
    </div>

    <div class="person">
      <p class="person__name">Melba Tran</p>
      <p class="person__title">Image Consultant</p>
    </div>
  </section>

  <section class="card card--back" aria-label="Business card back">
    <div class="brand">
      <span class="brand__name">KAL VERIA</span>
      <span class="brand__sub">CONSULTANCY</span>
    </div>
    <p class="website">www.<strong>kalveria</strong>.com.sg</p>
  </section>

</main>
</body>
</html>
```